Insight Plus. needs Business Cards

For this project, we need business cards (currently have also put a call out for a logo). We are a start-up called Insight Plus. This is our second company (our first one was called Querivance). Traditionally we have been providing market research services across different sectors, primarily financial services and the pharmaceutical industry. However, we now want to go beyond market research to offer more (Plus.)... strategic consulting and big data knowledge management. We want our brand to be approachable, creative, fun but professional.

Target Market(s)

The target audience is a business professional - we are B2B (business to business) and do not sell our services to individuals. The brands we work with are major brands across industries, but primarily automotive, financial and pharmaceutical.

Industry/Entity Type

Market Research

Font styles to use
Serif
Sans Serif
Other font styles liked:
• Calibri

Requirements
Must have
• Be clean, simple, modern
Show our address and phone number and email address and website URL
We do not need to have titles showing.

```html
<!DOCTYPE html>
<html lang="en">
<head>
<meta charset="utf-8">
<title>Insight Plus. — Business Cards</title>
<link rel="stylesheet" href="https://fonts.googleapis.com/css2?family=Open+Sans:wght@400;700&display=swap">
<style>
  :root {
    --teal: #1bb3a1;
    --ink: #111111;
    --paper: #ffffff;
    --paper-shade: #f2f2f2;
    --backdrop: #c9ccd1;
    --card-w: 540px;
    --card-h: 309px;
  }
  * { box-sizing: border-box; margin: 0; padding: 0; }
  html, body {
    width: 1200px; height: 866px; overflow: hidden;
    background: var(--backdrop);
    font-family: "Open Sans", Calibri, sans-serif;
  }
  .sheet {
    width: 1200px; height: 866px;
    display: flex; align-items: center; justify-content: center; gap: 40px;
  }
  .card {
    position: relative;
    width: var(--card-w); height: var(--card-h);
    overflow: hidden;
    box-shadow: 0 6px 18px rgba(0,0,0,0.18);
  }
  .card--front { background: var(--teal); }
  .card--back { background: linear-gradient(135deg, var(--paper) 40%, var(--paper-shade)); }
  .card__art { position: absolute; inset: 0; width: 100%; height: 100%; }
  .brand-name {
    position: absolute;
    color: var(--paper);
    font-weight: 400;
    white-space: nowrap;
    letter-spacing: 0.5px;
  }
  .card--front .brand-name { left: 120px; top: 126px; font-size: 44px; }
  .card--back .brand-name { left: 26px; top: 214px; font-size: 27px; }
  .contact {
    position: absolute; right: 26px; top: 26px;
    text-align: right; color: var(--ink);
    font-size: 12.5px; line-height: 1.45;
  }
  .contact__name { font-weight: 700; font-size: 15px; line-height: 1.2; }
  .contact__role { font-size: 14px; line-height: 1.2; margin-bottom: 40px; }
  .contact__address { margin-bottom: 12px; }
  .contact__line { display: flex; justify-content: flex-end; align-items: center; gap: 5px; }
  .contact__line svg { width: 11px; height: 11px; fill: var(--ink); }
  .contact__gap { height: 8px; }
</style>
</head>
<body>
<main class="sheet">
  <section class="card card--front" aria-label="Card front">
    <span class="brand-name">Insight Plus.</span>
  </section>

  <section class="card card--back" aria-label="Card back">
    <svg class="card__art" viewBox="0 0 540 309" aria-hidden="true">
      <path fill="var(--teal)" d="M0 0 L205 0 C 285 60, 282 230, 195 309 L0 309 Z"/>
      <path fill="var(--ink)" d="M218 0 C 318 60, 318 220, 236 309 L222 309 C 296 222, 296 70, 212 0 Z"/>
      <path fill="var(--ink)" d="M236 0 C 300 45, 312 170, 262 309 L254 309 C 296 170, 286 55, 228 0 Z"/>
    </svg>
    <span class="brand-name">Insight Plus.</span>

    <div class="contact">
      <p class="contact__name">Maren Holloway-Price</p>
      <p class="contact__role">Consultant</p>
      <p class="contact__address">12 Harbour Row, 4th floor<br>Kestrel Lane KSL</p>
      <p class="contact__line">020 555 0147
        <svg viewBox="0 0 24 24" aria-label="Phone"><path d="M6.6 10.8a15.1 15.1 0 0 0 6.6 6.6l2.2-2.2a1 1 0 0 1 1-.25 11.4 11.4 0 0 0 3.6.57 1 1 0 0 1 1 1V20a1 1 0 0 1-1 1A17 17 0 0 1 3 4a1 1 0 0 1 1-1h3.5a1 1 0 0 1 1 1 11.4 11.4 0 0 0 .57 3.6 1 1 0 0 1-.25 1z"/></svg>
      </p>
      <p class="contact__line">020 555 0148
        <svg viewBox="0 0 24 24" aria-label="Office phone"><path d="M4 8h16v13H4zM7 3h10v4H7zM7 11h2v2H7zm4 0h2v2h-2zm4 0h2v2h-2zM7 15h2v2H7zm4 0h2v2h-2zm4 0h2v2h-2z"/></svg>
      </p>
      <p class="contact__line">hello@insightplus.co
        <svg viewBox="0 0 24 24" aria-label="Email"><path d="M2 5h20v14H2zm2 2v.5l8 5 8-5V7l-8 5z"/></svg>
      </p>
      <div class="contact__gap"></div>
      <p class="contact__line">hello@insightplus.co</p>
      <p class="contact__line">www.insightplus.co</p>
    </div>
  </section>
</main>
</body>
</html>
```